" A Vasculária é uma clínica formada por profissionais especializados e em constante atualizaçao, capazes de atender as principais demandas de prevençao, diagnósticos e reabilitaçao da saúde vascular. Destaca-se por cuidar de pessoas e nao apenas tratar doenças. "

```html
<!DOCTYPE html>
<html lang="pt-BR">
<head>
<meta charset="utf-8">
<title>Vasculária – Cartão de Visita</title>
<link rel="stylesheet" href="https://fonts.googleapis.com/css2?family=Arimo:ital,wght@0,400;0,700;1,400&display=swap">
<style>
  :root {
    --page-bg: #eceae6;
    --card-bg: #ffffff;
    --brand-blue: #1f8fd1;
    --brand-blue-dark: #1670ad;
    --brand-blue-light: #4fb3ea;
    --text-dark: #3b3b3b;
    --text-muted: #6b6b6b;
    --icon-bg: #2a9ad8;
  }
  * { box-sizing: border-box; margin: 0; padding: 0; }
  html, body { width: 1200px; height: 1200px; overflow: hidden; }
  body {
    background: var(--page-bg);
    font-family: "Arimo", Arial, sans-serif;
    display: flex; flex-direction: column; align-items: center; justify-content: center;
    gap: 70px;
  }
  .card {
    width: 860px; height: 478px;
    background: var(--card-bg);
    position: relative; overflow: hidden;
    box-shadow: 0 10px 30px rgba(0,0,0,.12);
  }
  /* Front */
  .card-front .brand {
    position: absolute; left: 0; right: 0; top: 140px;
    text-align: center;
  }
  .brand-name {
    font-size: 76px; font-weight: 700; letter-spacing: 2px;
    color: var(--brand-blue);
  }
  .brand-tagline {
    margin-top: 4px;
    font-size: 22px; font-weight: 700; letter-spacing: 2.5px;
    color: var(--brand-blue);
  }
  .web-band {
    position: absolute; left: 0; right: 0; bottom: 0; height: 88px;
    background: linear-gradient(90deg, var(--brand-blue-dark), var(--brand-blue) 55%, var(--brand-blue-light));
    display: flex; align-items: center; justify-content: center;
  }
  .web-address {
    color: #fff; font-size: 30px; font-style: italic; letter-spacing: 3px;
  }
  /* Back */
  .side-strip {
    position: absolute; top: 0; right: 0; bottom: 0; width: 34px;
    background: linear-gradient(180deg, var(--brand-blue-light), var(--brand-blue-dark));
  }
  .person {
    position: absolute; left: 330px; top: 46px;
    color: var(--text-dark); font-size: 24px; line-height: 1.2;
  }
  .person .role, .person .reg { color: var(--text-muted); }
  .contact-list {
    position: absolute; left: 330px; top: 190px;
    list-style: none; display: flex; flex-direction: column; gap: 20px;
  }
  .contact-item {
    display: flex; align-items: center; gap: 12px;
    font-size: 23px; color: var(--text-dark);
  }
  .contact-icon {
    width: 40px; height: 40px; flex: none;
    background: var(--icon-bg); border-radius: 5px;
    display: flex; align-items: center; justify-content: center;
  }
  .contact-item.address { align-items: flex-start; line-height: 1.2; }
</style>
</head>
<body>

<section class="card card-front" aria-label="Frente do cartão">
  <div class="brand">
    <div class="brand-name">VASCULÁRIA</div>
    <div class="brand-tagline">ANGIOLOGIA E CIRURGIA VASCULAR</div>
  </div>
  <div class="web-band">
    <span class="web-address">www.vascularia.med.br</span>
  </div>
</section>

<section class="card card-back" aria-label="Verso do cartão">
  <div class="person">
    <div class="name">Nome Completo</div>
    <div class="role">Cargo</div>
    <div class="reg">CRM. 0000-00</div>
  </div>
  <ul class="contact-list">
    <li class="contact-item">
      <span class="contact-icon">
        <svg width="26" height="26" viewBox="0 0 24 24"><path fill="#fff" d="M6.6 10.8a15 15 0 0 0 6.6 6.6l2.2-2.2c.3-.3.7-.4 1-.2 1.1.4 2.3.6 3.6.6.6 0 1 .4 1 1V20c0 .6-.4 1-1 1A17 17 0 0 1 3 4c0-.6.4-1 1-1h3.5c.6 0 1 .4 1 1 0 1.3.2 2.5.6 3.6.1.3 0 .7-.2 1z"/></svg>
      </span>
      Tel. (00) 0000 - 0000
    </li>
    <li class="contact-item">
      <span class="contact-icon">
        <svg width="26" height="26" viewBox="0 0 24 24"><rect x="3" y="6" width="18" height="12" rx="1" fill="none" stroke="#fff" stroke-width="1.8"/><path d="M3 7l9 6 9-6" fill="none" stroke="#fff" stroke-width="1.8"/></svg>
      </span>
      contato@vascularia.med.br
    </li>
    <li class="contact-item">
      <span class="contact-icon">
        <svg width="22" height="22" viewBox="0 0 24 24"><rect x="5" y="5" width="14" height="14" fill="#fff"/></svg>
      </span>
      contato@vascularia.med.br
    </li>
    <li class="contact-item address">
      <span class="contact-icon">
        <svg width="26" height="26" viewBox="0 0 24 24"><path fill="#fff" d="M12 2a6 6 0 0 0-6 6c0 4.5 6 12 6 12s6-7.5 6-12a6 6 0 0 0-6-6zm0 8.3a2.3 2.3 0 1 1 0-4.6 2.3 2.3 0 0 1 0 4.6z"/></svg>
      </span>
      <span>Rua das Acácias nº 1000,<br>Centro - SP</span>
    </li>
  </ul>
  <div class="side-strip"></div>
</section>

</body>
</html>
```